Website Re-design

Hi, I'm looking for help in redesigning my web site. I currently have a site www.brightnookwares.example where I sell lamps, and while I like some aspects of the design, you can tell that I have done the graphics myself and am not a pro at it. I'd like help in redesigning it, and am open to completely new design graphics. I have made the 3 slider images myself, and I feel they could be a bit better, but I am not sure how to do it. For example, on the homepage, the 'About Us', 'Secured Shopping', and '$10 Off' graphics don't go well with the rest of the page. I would like more cohesion in the design and more visual interest in the header, which is pretty basic right now. Also, that the bottom footer is black, I would like instead something else. I am looking for just the layout of the homepage, and possibly once that is done to work on more visual interest in some of the informational pages and product pages. I am looking for just the design in the form of a photoshop file or files that I can incorporate into my site. Thank you!

Reason: I just made this project payment committed, so I'd like a chance for designers who only choose payment committed projects to submit artwork. Thank you.

This project is now payment guaranteed/ committed.  Thanks.

```html
<!DOCTYPE html>
<html lang="en">
<head>
<meta charset="utf-8">
<title>Bright Nook — Home</title>
<link href="https://fonts.googleapis.com/css2?family=Lobster&family=Source+Sans+3:wght@300;400;600;700&family=Tinos&display=swap" rel="stylesheet">
<style>
  :root {
    --topbar: #2b2b2b;
    --topbar-text: #c9c9c9;
    --ink: #3f3f3f;
    --ink-soft: #555;
    --teal: #4db3c8;
    --teal-deep: #1f7d87;
    --red: #e8202a;
    --green: #7ab36c;
    --orange: #e0480f;
    --orange-edge: #a83406;
    --footer: #e6e6e6;
    --rule: #cfcfcf;
    --white: #ffffff;
  }
  * { box-sizing: border-box; margin: 0; padding: 0; }
  html, body { width: 1034px; height: 1200px; overflow: hidden; }
  body { position: relative; font-family: "Source Sans 3", sans-serif; color: var(--ink); background: var(--white); }
  .abs { position: absolute; }

  /* top bar */
  .topbar { left: 0; top: 0; width: 1034px; height: 44px; background: var(--topbar); border-bottom: 1px solid #111; }
  .topbar-link { top: 13px; font-size: 12px; color: var(--topbar-text); }
  .topbar-link.strong { color: var(--white); font-weight: 700; }
  .topbar-divider { left: 754px; top: 4px; width: 1px; height: 36px; background: #555; }
  .search { left: 767px; top: 11px; width: 136px; height: 23px; border-radius: 12px; background: #555; box-shadow: inset 0 1px 3px #000; font-size: 12px; color: #bbb; padding: 4px 12px; }
  .search svg { position: absolute; right: 9px; top: 5px; }

  /* header */
  .brand { left: 136px; top: 76px; display: flex; align-items: center; gap: 10px; }
  .brand-mark { width: 36px; height: 36px; border: 3px solid var(--ink); border-radius: 50%; }
  .brand-name { font-size: 27px; font-weight: 600; color: var(--ink); line-height: 1; }
  .cart { left: 538px; top: 68px; display: flex; align-items: center; gap: 6px; font-size: 13px; color: var(--ink-soft); }
  .cart-heart { left: 648px; top: 56px; }
  .cart-count { left: 666px; top: 69px; font-size: 12px; color: #e4572e; }
  .cart-items { left: 698px; top: 68px; font-size: 13px; color: var(--ink-soft); }
  .checkout { left: 734px; top: 64px; width: 81px; height: 26px; border: 1px solid #bbb; border-radius: 3px; background: linear-gradient(#f7f7f7, #dcdcdc); font-size: 14px; text-align: center; line-height: 24px; color: var(--ink); }
  .nav { left: 315px; top: 99px; width: 598px; height: 41px; border: 1px solid #e6e6e6; box-shadow: 0 1px 2px rgba(0,0,0,.08); background: var(--white); }
  .nav-item { top: 10px; font-size: 16px; font-weight: 300; color: #555; letter-spacing: .2px; }
  .wishlist-art { left: 843px; top: 66px; width: 52px; height: 68px; background: linear-gradient(#fafafa, #e2e2e2); transform: rotate(-6deg); box-shadow: 0 2px 4px rgba(0,0,0,.2); }

  /* hero */
  .hero { left: 0; top: 154px; width: 1034px; height: 559px; background:
      linear-gradient(180deg, transparent 0 72%, #d9dcdc 72%, #eef0f0 76%, #b9c0c2 100%),
      radial-gradient(ellipse at 62% 30%, #a9dcdd 0%, #4aa3ab 45%, #1f6f78 100%); }
  .hero-lamp { left: 600px; top: 214px; width: 240px; height: 430px; background: linear-gradient(180deg, #f4f2ee 0 34%, #3aa8c7 34%, #2fa0c2 75%, #7fc06a 90%, #dfe6e8 100%); border-radius: 8px 8px 40px 40px; opacity: .9; }
  .hero-title { left: 140px; width: 330px; text-align: center; font-family: "Lobster", cursive; color: var(--white); text-shadow: 0 2px 3px rgba(0,0,0,.2); line-height: 1; }
  .hero-rule { top: 301px; height: 3px; border-top: 1px solid rgba(255,255,255,.6); border-bottom: 1px solid rgba(255,255,255,.6); }
  .hero-sub { left: 138px; width: 330px; top: 418px; text-align: center; font-family: "Tinos", serif; font-size: 24px; color: var(--white); text-shadow: 0 1px 2px rgba(0,0,0,.3); }
  .hero-cta { left: 192px; top: 475px; width: 219px; height: 46px; background: linear-gradient(#f0581c, var(--orange)); border: 1px solid var(--orange-edge); border-radius: 4px; box-shadow: 0 2px 0 var(--orange-edge); text-align: center; font-family: "Tinos", serif; font-size: 23px; line-height: 44px; color: var(--white); }
  .dot { top: 565px; width: 9px; height: 9px; border-radius: 50%; background: var(--white); }
  .dot.active { background: #111; }

  /* feature cards */
  .features { left: 0; top: 713px; width: 1034px; height: 253px; background: linear-gradient(#ffffff, #f2f2f0); }
  .card { top: 684px; width: 247px; height: 240px; }
  .card-band { position: absolute; left: 0; top: 30px; width: 247px; height: 86px; border-top: 2px solid var(--white); box-shadow: inset 0 2px 0 rgba(0,0,0,.08); }
  .card-band::after { content: ""; position: absolute; left: 0; bottom: -4px; width: 100%; height: 4px; background: radial-gradient(circle at 3px 0, var(--band) 3px, transparent 3.5px) 0 0 / 6px 4px repeat-x; }
  .card-hex { position: absolute; left: 94px; top: 0; }
  .card-title { position: absolute; left: 0; top: 68px; width: 100%; text-align: center; font-family: "Lobster", cursive; font-size: 29px; color: var(--white); }
  .card-text { position: absolute; left: 0; top: 136px; width: 100%; text-align: center; font-size: 15px; line-height: 19px; color: var(--ink-soft); }
  .card-btn { position: absolute; left: 84px; top: 209px; width: 79px; height: 24px; text-align: center; font-size: 12px; line-height: 24px; color: var(--white); }
  .about { left: 130px; --band: var(--teal); }
  .secure { left: 393px; --band: var(--red); }
  .offer { left: 656px; --band: var(--green); }
  .card-band, .card-btn { background: var(--band); }

  /* footer */
  .footer { left: 0; top: 966px; width: 1034px; height: 234px; background: linear-gradient(135deg, #e9e9e9, #e0e0e0 60%, #e8e8e8); }
  .footer-col { top: 994px; width: 112px; }
  .footer-col h3 { font-size: 13px; font-weight: 400; color: #222; padding-bottom: 6px; border-bottom: 1px solid var(--rule); margin-bottom: 8px; }
  .footer-col li { list-style: none; font-size: 12px; line-height: 20px; color: #444; }
  .signup { left: 697px; top: 994px; width: 215px; }
  .signup h3 { font-size: 13px; font-weight: 400; color: #222; }
  .signup-field { position: absolute; left: 0; top: 25px; width: 148px; height: 26px; background: var(--white); border: 1px solid #222; font-size: 11px; padding: 5px 6px; color: #222; }
  .signup-btn { position: absolute; left: 148px; top: 25px; }
  .signup-note { position: absolute; left: 0; top: 60px; font-size: 12px; color: #444; white-space: nowrap; }
  .social { top: 1088px; width: 33px; height: 33px; border-radius: 50%; background: linear-gradient(#7d8791, #4d5660); box-shadow: 0 1px 2px rgba(0,0,0,.3); }
  .footer-rule { left: 120px; top: 1154px; width: 792px; height: 1px; background: var(--rule); }
  .copyright { left: 0; width: 1034px; top: 1168px; text-align: center; font-size: 12px; color: #444; }
</style>
</head>
<body>

<!-- top utility bar -->
<div class="abs topbar"></div>
<span class="abs topbar-link strong" style="left:515px">Sign In</span>
<span class="abs topbar-link" style="left:563px">or</span>
<span class="abs topbar-link" style="left:587px">Create an account</span>
<span class="abs topbar-link" style="left:685px">My Account</span>
<div class="abs topbar-divider"></div>
<div class="abs search">Search
  <svg width="13" height="13" viewBox="0 0 13 13"><circle cx="5" cy="5" r="4" fill="none" stroke="#111" stroke-width="2"/><line x1="8" y1="8" x2="12" y2="12" stroke="#111" stroke-width="2"/></svg>
</div>

<!-- header -->
<div class="abs brand"><span class="brand-mark"></span><span class="brand-name">bright nook</span></div>
<div class="abs cart">
  <svg width="24" height="18" viewBox="0 0 24 18"><path d="M1 2h4l3 10h12l2-7H7" fill="none" stroke="#2a9fb5" stroke-width="2"/><circle cx="10" cy="15.5" r="1.6" fill="#2a9fb5"/><circle cx="18" cy="15.5" r="1.6" fill="#2a9fb5"/></svg>
  Shopping Cart
</div>
<svg class="abs cart-heart" width="46" height="46" viewBox="0 0 46 46"><path d="M23 40 C6 28 2 20 4 12 C7 4 17 4 23 13 C29 4 39 4 42 12 C44 20 40 28 23 40 Z" fill="none" stroke="#9a9a9a" stroke-width="1.5"/></svg>
<span class="abs cart-count">0</span>
<span class="abs cart-items">Items</span>
<div class="abs checkout">Checkout</div>
<nav class="abs nav"></nav>
<span class="abs nav-item" style="left:337px;top:109px">HOME</span>
<span class="abs nav-item" style="left:407px;top:109px">SHOP</span>
<span class="abs nav-item" style="left:471px;top:109px">ABOUT US</span>
<span class="abs nav-item" style="left:566px;top:109px">CONTACT US</span>
<span class="abs nav-item" style="left:749px;top:109px">MY WISHLIST</span>
<div class="abs wishlist-art" role="img" aria-label="Wishlist note paper with a small heart"></div>

<!-- hero slider -->
<div class="abs hero" role="img" aria-label="Photo of a blue glass table lamp with a white shade standing on whitewashed wooden floorboards against a teal wall"></div>
<div class="abs hero-lamp" role="img" aria-label="Table lamp product photo"></div>
<div class="abs hero-title" style="top:198px;font-size:72px">Light Up</div>
<div class="abs hero-rule" style="left:138px;width:108px"></div>
<div class="abs hero-rule" style="left:356px;width:108px"></div>
<div class="abs hero-title" style="top:284px;font-size:40px">the</div>
<div class="abs hero-title" style="top:320px;font-size:72px">Room</div>
<div class="abs hero-sub">"The Lagoon" Medium Table Lamp</div>
<div class="abs hero-cta">SHOP ALL LAMPS</div>
<span class="abs dot active" style="left:283px"></span>
<span class="abs dot" style="left:298px"></span>
<span class="abs dot" style="left:313px"></span>

<!-- feature cards -->
<div class="abs features"></div>

<section class="abs card about">
  <div class="card-band"></div>
  <svg class="card-hex" width="60" height="66" viewBox="0 0 60 66"><polygon points="30,2 57,17 57,49 30,64 3,49 3,17" fill="var(--teal)" stroke="#fff" stroke-width="2"/><circle cx="30" cy="27" r="6" fill="#fff"/><path d="M19 44 C19 35 41 35 41 44 Z" fill="#fff"/></svg>
  <div class="card-title">About Us</div>
  <p class="card-text">Bright Nook provides beautiful and<br>artistic home and hospitality lighting.</p>
  <div class="card-btn">READ MORE</div>
</section>

<section class="abs card secure">
  <div class="card-band"></div>
  <svg class="card-hex" width="60" height="66" viewBox="0 0 60 66"><polygon points="30,2 57,17 57,49 30,64 3,49 3,17" fill="var(--red)" stroke="#fff" stroke-width="2"/><path d="M13 25h4l3 10h10" fill="none" stroke="#fff" stroke-width="2.5"/><circle cx="21" cy="40" r="2" fill="#fff"/><circle cx="29" cy="40" r="2" fill="#fff"/><rect x="33" y="31" width="12" height="10" fill="#fff"/><path d="M35 31v-3a4 4 0 0 1 8 0v3" fill="none" stroke="#fff" stroke-width="2"/></svg>
  <div class="card-title">Secured Shopping</div>
  <p class="card-text">Shopping at Bright Nook is secured<br>and protected by industry standard best<br>practices.</p>
  <div class="card-btn">READ MORE</div>
</section>

<section class="abs card offer">
  <div class="card-band"></div>
  <svg class="card-hex" width="60" height="66" viewBox="0 0 60 66"><polygon points="30,2 57,17 57,49 30,64 3,49 3,17" fill="var(--green)" stroke="#fff" stroke-width="2"/><rect x="16" y="24" width="28" height="19" fill="#fff"/><path d="M16 24 L30 35 L44 24" fill="none" stroke="var(--green)" stroke-width="2"/></svg>
  <div class="card-title">$10 Off</div>
  <p class="card-text">$10 off any purchase when you sign up for<br>our newsletter.</p>
  <div class="card-btn">SIGN UP</div>
</section>

<!-- footer -->
<footer class="abs footer"></footer>
<div class="abs footer-col" style="left:120px"><h3>HELP + INFO</h3><ul><li>Contact Us</li><li>Shipping Info</li><li>Returns</li><li>To The Trade</li><li>Privacy Policy</li><li>Terms of Use</li></ul></div>
<div class="abs footer-col" style="left:255px"><h3>MY ACCOUNT</h3><ul><li>Sign In</li><li>Order Status</li><li>Order History</li><li>View Cart</li><li>Checkout</li></ul></div>
<div class="abs footer-col" style="left:390px"><h3>ABOUT</h3><ul><li>Who We Are</li><li>Testimonials</li></ul></div>
<div class="abs footer-col" style="left:525px;width:140px"><h3>CONTACT</h3><ul><li>Contact Us</li><li>info@brightnookwares.example</li></ul></div>

<div class="abs signup">
  <h3>SIGN UP FOR BRIGHT NOOK EMAILS</h3>
  <div class="signup-field">Enter your email</div>
  <svg class="signup-btn" width="66" height="26" viewBox="0 0 66 26"><polygon points="0,0 56,0 66,13 56,26 0,26" fill="#111"/><text x="28" y="17" text-anchor="middle" font-family="Source Sans 3, sans-serif" font-weight="700" font-size="12" fill="#fff">JOIN US</text></svg>
  <p class="signup-note">Because you love being the first to know</p>
</div>
<a class="abs social" style="left:697px" aria-label="Social network link"></a>
<a class="abs social" style="left:739px" aria-label="Social network link"></a>
<a class="abs social" style="left:781px" aria-label="Social network link"></a>

<div class="abs footer-rule"></div>
<p class="abs copyright">© 2013 Bright Nook.&nbsp; All Rights Reserved</p>

</body>
</html>
```